Brochure design for 3D ultrasound company

I am looking for a clean and modern and edgy brochure for my ultrasound company. We are a fairly new company specialize in 3D/4D ultrasounds.Our brochures will be placed in OB-GYN offices in high end areas around Los Angeles, so we need something that will stand out and capture a modern woman's attention. Our logo is currently in the process of being designed, so I don't have a picture to provide quite yet, however it will be our company name"Kite + Fern" written in a special font that looks like neon lights. I will attach a few images of what our logo will be like, and some initial content that can help provide the layout we would like for the brochure. please feel free to also take a look at our website. www.kitefernscans.example.

Target Market(s)

Upscale trendy women.

Colors
eea4c8
33a6d7
fee18a

Requirements
Should not have
• too many colors.

```html
<!DOCTYPE html>
<html lang="en">
<head>
<meta charset="utf-8">
<title>Kite + Fern — Services + Pricing Brochure</title>
<link rel="stylesheet" href="https://fonts.googleapis.com/css2?family=Lobster+Two:ital,wght@1,700&family=Montserrat:wght@400;500;600;700&display=swap">
<style>
  :root {
    --pink: #eea4c8;
    --pink-soft: #f6cfe2;
    --blue: #33a6d7;
    --red: #e3183b;
    --ink: #1d1d1f;
    --white: #ffffff;
    --script: "Lobster Two", cursive;
    --sans: "Montserrat", sans-serif;
  }
  * { margin: 0; padding: 0; box-sizing: border-box; }
  html, body { width: 1200px; height: 931px; overflow: hidden; background: #e4e4e6; }
  .brochure {
    position: relative; width: 1200px; height: 931px;
    background: var(--white); font-family: var(--sans); color: var(--ink);
  }
  .backdrop { position: absolute; inset: 0; }
  .panel { position: absolute; top: 0; width: 400px; height: 931px; text-align: center; }
  .panel--left { left: 0; }
  .panel--middle { left: 400px; }
  .panel--right { left: 800px; }
  .fold { position: absolute; top: 0; width: 1px; height: 931px; background: rgba(0,0,0,.06); }

  .photo { position: absolute; }
  .photo--couple {
    left: 55px; top: 30px; width: 290px; height: 290px; border-radius: 50%;
    background: linear-gradient(160deg, #e9d5c4 0%, #b8c3d3 45%, #5f7fa6 75%, #36503f 100%);
    box-shadow: 0 0 0 12px var(--pink-soft);
  }
  .photo--mother {
    left: 60px; top: 240px; width: 290px; height: 691px;
    border-radius: 140px 140px 0 0;
    background: linear-gradient(180deg, #e8c5a8 0%, #f4f4f4 25%, #f3f3f3 50%, #efc0ad 62%, #4f77a5 78%, #2f5a8c 100%);
  }
  .photo--bellies {
    left: 0; top: 575px; width: 400px; height: 356px;
    background: linear-gradient(135deg, #f2c7c2 0%, #f0b5ad 35%, #f7d8cc 55%, #9cbbd8 80%, #7aa3cb 100%);
  }

  .script { font-family: var(--script); font-style: italic; font-weight: 700; }
  .package-title { font-weight: 700; color: var(--red); letter-spacing: .04em; text-transform: uppercase; }
  .price { font-weight: 600; color: var(--blue); }
  .price sup { font-size: .5em; vertical-align: .8em; margin-right: 1px; }

  .bracket { position: relative; margin: 0 auto; padding: 6px 0 10px; }
  .bracket::before, .bracket::after { content: ""; position: absolute; width: 46%; height: 22px; }
  .bracket::before { top: 4px; right: 0; border-top: 1.5px solid var(--bracket, var(--blue)); border-right: 1.5px solid var(--bracket, var(--blue)); border-top-right-radius: 6px; }
  .bracket::after { bottom: 0; left: 0; border-bottom: 1.5px solid var(--bracket, var(--blue)); border-left: 1.5px solid var(--bracket, var(--blue)); border-bottom-left-radius: 6px; }

  .features { list-style: none; font-size: 13px; line-height: 1.35; }
  .features li::before { content: "●"; font-size: 9px; margin-right: 5px; vertical-align: 2px; color: var(--dot, var(--blue)); }

  /* left panel */
  .popular { position: absolute; left: 0; top: 440px; width: 400px; color: var(--white); }
  .popular__heading { font-size: 38px; line-height: 1.05; }
  .popular .bracket { width: 300px; margin-top: 14px; --bracket: var(--white); }
  .popular .package-title { font-size: 24px; }
  .popular .price { color: var(--white); font-size: 20px; }
  .popular .features { margin-top: 12px; font-size: 13.5px; --dot: var(--white); }
  .contact { position: absolute; left: 0; top: 735px; width: 400px; }
  .contact__lead { font-size: 13px; font-weight: 600; line-height: 1.35; }
  .contact__phone { display: flex; justify-content: center; align-items: center; gap: 8px; margin-top: 8px; color: var(--white); font-size: 34px; font-weight: 500; letter-spacing: .02em; }
  .contact__phone svg { width: 26px; height: 26px; }
  .contact__web-lead { margin-top: 6px; font-size: 13px; font-weight: 600; }
  .contact__web { color: var(--red); font-size: 16px; font-weight: 600; margin-top: 2px; }

  /* middle panel */
  .services { position: absolute; left: 0; top: 40px; width: 400px; }
  .services__heading { color: var(--blue); font-size: 42px; }
  .services__intro { margin: 8px auto 0; width: 300px; font-size: 12px; line-height: 1.4; }

  /* right panel */
  .packages { position: absolute; left: 40px; top: 40px; width: 320px; }
  .package { margin-bottom: 30px; }
  .package .package-title { font-size: 20px; }
  .package .price { font-size: 18px; }
  .package .features { margin-top: 6px; }
</style>
</head>
<body>
<main class="brochure">
  <svg class="backdrop" width="1200" height="931" viewBox="0 0 1200 931" aria-hidden="true">
    <path d="M0 300 C120 270 250 400 400 415 C560 430 700 420 800 470 C900 520 1050 555 1200 545 L1200 931 L0 931 Z" fill="var(--pink-soft)"/>
    <path d="M0 325 C120 295 250 420 400 435 C560 450 700 440 800 490 C900 540 1050 572 1200 565 L1200 931 L0 931 Z" fill="var(--pink)"/>
  </svg>

  <section class="panel panel--left">
    <div class="photo photo--couple" role="img" aria-label="Photo: couple holding BOY and GIRL notes over a pregnant belly in denim overalls"></div>
    <div class="popular">
      <h2 class="popular__heading script">Our Most<br>Popular Package</h2>
      <div class="bracket">
        <h3 class="package-title">The Big Reveal!!</h3>
        <p class="price"><sup>$</sup>225.00</p>
      </div>
      <ul class="features">
        <li>25 minute 3D/4D/HD live session</li>
        <li>5 black and white pictures</li>
        <li>5 color pictures</li>
        <li>Email or USB flash drive with all images</li>
        <li>Record and hear heartbeat</li>
        <li>Confirm gender</li>
      </ul>
    </div>
    <div class="contact">
      <p class="contact__lead">Ready for your baby’s<br>first photoshoot?<br>Give us a call to schedule an appointment</p>
      <p class="contact__phone">
        <svg viewBox="0 0 26 26" aria-hidden="true"><circle cx="13" cy="13" r="13" fill="var(--white)"/><path d="M9 7c1 0 2 2.5 2 3s-1 1-1 1.5 2 4 4.5 4.5c.5 0 1-1 1.5-1s3 1 3 2-1.5 2.5-2.5 2.5C11 19.5 6.5 15 6.5 10c0-1 1.5-3 2.5-3z" fill="var(--pink)"/></svg>
        (555) 014-2290
      </p>
      <p class="contact__web-lead">or visit our website</p>
      <p class="contact__web">www.kitefernscans.example</p>
    </div>
  </section>

  <section class="panel panel--middle">
    <div class="services">
      <h1 class="services__heading script">Services + Pricing</h1>
      <p class="services__intro">We are available for private in-home screenings, gender reveals, baby showers, or any other special occasion!</p>
    </div>
    <div class="photo photo--mother" role="img" aria-label="Photo: pregnant woman in white t-shirt and jeans, hand raised playfully over her eyes"></div>
  </section>

  <section class="panel panel--right">
    <div class="packages">
      <article class="package">
        <div class="bracket">
          <h3 class="package-title">Peek-a-boo</h3>
          <p class="price"><sup>$</sup>125.00</p>
        </div>
        <ul class="features">
          <li>15 minute 2D session</li>
          <li>3 black and white images</li>
          <li>Listen to baby’s heartbeat</li>
          <li>Confirm gender</li>
        </ul>
      </article>
      <article class="package">
        <div class="bracket">
          <h3 class="package-title">Hello, Momma</h3>
          <p class="price"><sup>$</sup>165.00</p>
        </div>
        <ul class="features">
          <li>15 minute 3D/4D /HD live session</li>
          <li>3 black and white images</li>
          <li>2 color images</li>
          <li>Listen to baby’s heartbeat</li>
          <li>Confirm gender</li>
        </ul>
      </article>
      <article class="package">
        <div class="bracket">
          <h3 class="package-title">V.I.B<br>(Very Important Baby)</h3>
          <p class="price"><sup>$</sup>325.00</p>
        </div>
        <ul class="features">
          <li>30 min 3D/4D/HD live session on our projector</li>
          <li>10 color images</li>
          <li>Email or USB with all images</li>
          <li>Record and hear heartbeat</li>
          <li>Confirm gender</li>
        </ul>
      </article>
    </div>
    <div class="photo photo--bellies" role="img" aria-label="Photo: two pregnant bellies side by side in crop tops and open jeans"></div>
  </section>

  <div class="fold" style="left:400px"></div>
  <div class="fold" style="left:800px"></div>
</main>
</body>
</html>
```